digger and truck hire

this is a new business - Digger and Truck
we would like to include the attached photo of the digger and truck - as the truck is red and the digger is green
maybe either black or white lettering which ever suits

Business

Contact Information for Business Card

RDL - Bodrins 2.5t Mini Digger and 7t Tip Truck -Hire, full attachments, augers, trenching, site preparation, small aggregate deliveries
Phone 0261593847
bodrin.rdl@velmo.co.nz

```html
<!DOCTYPE html>
<html lang="en">
<head>
<meta charset="utf-8">
<title>RDL Business Card</title>
<link rel="stylesheet" href="https://fonts.googleapis.com/css2?family=Comfortaa:wght@400;700&display=swap">
<style>
  :root {
    --page-bg: #ececec;
    --card-white: #ffffff;
    --brand-red: #e0452a;
    --brand-red-dark: #c7361d;
    --ink: #2a2a2a;
    --text-light: #ffffff;
    --text-outline: #1d1d1d;
  }
  html, body {
    margin: 0;
    padding: 0;
    width: 1200px;
    height: 1200px;
    overflow: hidden;
    background: var(--page-bg);
    font-family: "Comfortaa", sans-serif;
  }
  .business-card {
    position: absolute;
    left: 60px;
    top: 291px;
    width: 1080px;
    height: 617px;
    background: var(--card-white);
    overflow: hidden;
    box-shadow: 0 6px 18px rgba(0,0,0,0.25);
  }
  .card-header {
    position: absolute;
    left: 0; top: 0;
    width: 100%;
    height: 140px;
  }
  .brand-name {
    position: absolute;
    left: 60px;
    top: 28px;
    display: flex;
    align-items: center;
    gap: 14px;
    color: var(--brand-red);
    font-weight: 700;
    font-size: 72px;
    line-height: 1;
  }
  .brand-mark {
    width: 22px;
    height: 22px;
    background: var(--brand-red);
  }
  .business-title {
    position: absolute;
    left: 300px;
    top: 72px;
    margin: 0;
    font-weight: 400;
    font-size: 27px;
    letter-spacing: 0.5px;
    color: var(--ink);
    text-transform: uppercase;
    white-space: nowrap;
  }
  .header-rule {
    position: absolute;
    left: 40px;
    right: 0;
    top: 118px;
    height: 6px;
    background: var(--brand-red);
  }
  .photo-area {
    position: absolute;
    left: 0; top: 140px;
    width: 100%;
    height: 477px;
    background:
      linear-gradient(180deg, rgba(255,255,255,0) 60%, rgba(160,80,35,0.55) 100%),
      linear-gradient(100deg, #c9342b 0%, #b9423a 28%, #6f8598 44%, #98a8b4 58%, #5f7d74 70%, #8e9ca8 82%, #a65a2b 100%);
  }
  .service-list {
    position: absolute;
    left: 70px;
    top: 200px;
    margin: 0;
    padding: 0;
    list-style: none;
  }
  .service-list li {
    display: flex;
    align-items: center;
    gap: 10px;
    height: 50px;
    font-size: 32px;
    color: var(--text-light);
    text-shadow: -1px -1px 0 var(--text-outline), 1px -1px 0 var(--text-outline), -1px 1px 0 var(--text-outline), 1px 1px 0 var(--text-outline), 0 2px 4px rgba(0,0,0,0.5);
    white-space: nowrap;
  }
  .tick-box { width: 32px; height: 32px; flex: none; }
  .contact-list {
    position: absolute;
    left: 520px;
    top: 200px;
  }
  .contact-item {
    display: flex;
    align-items: center;
    gap: 14px;
    height: 80px;
    font-size: 34px;
    color: var(--text-light);
    text-shadow: -1px -1px 0 var(--text-outline), 1px -1px 0 var(--text-outline), -1px 1px 0 var(--text-outline), 1px 1px 0 var(--text-outline), 0 2px 4px rgba(0,0,0,0.5);
    white-space: nowrap;
  }
  .contact-icon { width: 62px; height: 62px; flex: none; }
</style>
</head>
<body>
  <div class="business-card">
    <header class="card-header">
      <div class="brand-name"><span class="brand-mark"></span>RDL</div>
      <h1 class="business-title">Bodrins 2.5t Mini Digger and 7t Tip Truck-Hire</h1>
      <div class="header-rule"></div>
    </header>

    <div class="photo-area" role="img" aria-label="Photo of the red tip truck carrying the green mini digger strapped on its tray"></div>

    <ul class="service-list">
      <li><svg class="tick-box" viewBox="0 0 32 32"><rect x="2" y="6" width="24" height="24" fill="#fff" stroke="var(--brand-red)" stroke-width="3"/><path d="M8 17 L14 24 L29 4" fill="none" stroke="var(--brand-red)" stroke-width="4" stroke-linecap="round" stroke-linejoin="round"/></svg>Full Attachment</li>
      <li><svg class="tick-box" viewBox="0 0 32 32"><rect x="2" y="6" width="24" height="24" fill="#fff" stroke="var(--brand-red)" stroke-width="3"/><path d="M8 17 L14 24 L29 4" fill="none" stroke="var(--brand-red)" stroke-width="4" stroke-linecap="round" stroke-linejoin="round"/></svg>Augers</li>
      <li><svg class="tick-box" viewBox="0 0 32 32"><rect x="2" y="6" width="24" height="24" fill="#fff" stroke="var(--brand-red)" stroke-width="3"/><path d="M8 17 L14 24 L29 4" fill="none" stroke="var(--brand-red)" stroke-width="4" stroke-linecap="round" stroke-linejoin="round"/></svg>Trenching</li>
      <li><svg class="tick-box" viewBox="0 0 32 32"><rect x="2" y="6" width="24" height="24" fill="#fff" stroke="var(--brand-red)" stroke-width="3"/><path d="M8 17 L14 24 L29 4" fill="none" stroke="var(--brand-red)" stroke-width="4" stroke-linecap="round" stroke-linejoin="round"/></svg>Site Preparation</li>
      <li><svg class="tick-box" viewBox="0 0 32 32"><rect x="2" y="6" width="24" height="24" fill="#fff" stroke="var(--brand-red)" stroke-width="3"/><path d="M8 17 L14 24 L29 4" fill="none" stroke="var(--brand-red)" stroke-width="4" stroke-linecap="round" stroke-linejoin="round"/></svg>Small Aggregate Deliveries</li>
    </ul>

    <div class="contact-list">
      <div class="contact-item">
        <svg class="contact-icon" viewBox="0 0 62 62">
          <circle cx="31" cy="31" r="28" fill="#fff" stroke="var(--brand-red)" stroke-width="4"/>
          <path d="M22 16 c2-1 4 0 5 2 l3 6 c1 2 0 3-1 4 l-2 2 c2 4 5 7 9 9 l2-2 c1-1 2-2 4-1 l6 3 c2 1 3 3 2 5 l-2 3 c-2 2-5 3-8 2 C29 46 17 34 14 25 c-1-3 0-6 2-8 z" fill="var(--brand-red)"/>
        </svg>
        <span class="contact-text">0261593847</span>
      </div>
      <div class="contact-item">
        <svg class="contact-icon" viewBox="0 0 62 62">
          <circle cx="31" cy="31" r="28" fill="#fff" stroke="var(--brand-red)" stroke-width="4"/>
          <rect x="16" y="20" width="30" height="22" fill="none" stroke="var(--brand-red)" stroke-width="3"/>
          <path d="M16 20 L31 33 L46 20 M16 42 L27 30 M46 42 L35 30" fill="none" stroke="var(--brand-red)" stroke-width="3"/>
        </svg>
        <span class="contact-text">bodrin.rdl@velmo.co.nz</span>
      </div>
    </div>
  </div>
</body>
</html>
```